Web Design + logo Project

hi,
we are based in ASEAN region (Malaysia/Indonesia/Singapore), involving in Online Vehicle Insurance Portal. so far our product is only car insurance and personal insurance, and motorbikes insurance)
We need a webdesign + logo for KotaLindung.com
The website is www.kotalindung.example. The website is already up with the necessary quotation comparison + purchase mechanism.
We like www.vantorelo.example look and feel very much.
Blue is the preferred main theme.
The mainpage should highlight the following
1) quotation generator/input
2) hotline number
3) news/testimonial
The webdesign should be able to cater for mobile users as well.
The design should be professional and energetic
Target Market(s)
20-35years old vehicle owners in Indonesia/thailand/Singapore/vietnam
Industry/Entity Type
Car Insurance
Look and feel
Each slider illustrates characteristics of the customer's brand and the style your logo design should communicate.

```html
<!DOCTYPE html>
<html lang="en">
<head>
<meta charset="utf-8">
<title>KotaLindung — Vehicle Insurance</title>
<link rel="stylesheet" href="https://fonts.googleapis.com/css2?family=PT+Sans:ital,wght@0,400;0,700;1,700&family=Arimo:wght@400;700&display=swap">
<style>
  :root {
    --blue: #3a7dbd;
    --blue-dark: #2c5f96;
    --blue-deep: #1f4d7d;
    --blue-light: #4a8cc9;
    --green: #9dd445;
    --green-light: #b4df5f;
    --green-dark: #8cc63c;
    --navy-text: #1f3a5c;
    --white: #ffffff;
    --sky-top: #5ea2e6;
    --sky-pale: #d6e9f8;
  }
  * { margin: 0; padding: 0; box-sizing: border-box; }
  html, body { width: 1200px; height: 1000px; overflow: hidden; background: var(--white); }
  body { position: relative; font-family: "PT Sans", sans-serif; }
  .abs { position: absolute; }

  .brand { left: 213px; top: 40px; display: flex; align-items: center; gap: 14px; }
  .brand-name { font-size: 50px; font-weight: 700; color: var(--blue); letter-spacing: -0.5px; line-height: 1; }
  .brand-mark { width: 22px; height: 22px; background: var(--green); }
  .hotline { right: 172px; top: 48px; font-size: 38px; font-weight: 700; color: var(--green); line-height: 1; letter-spacing: 0.5px; }

  .main-nav { left: 160px; top: 119px; width: 880px; height: 34px; background: linear-gradient(var(--blue-light), var(--blue-dark)); }
  .nav-home { position: absolute; left: 3px; top: 4px; width: 128px; height: 27px; }
  .nav-item { position: absolute; top: 7px; font-size: 15px; color: var(--white); }
  .nav-item.active { color: var(--blue); }
  .search { position: absolute; left: 703px; top: 6px; width: 165px; height: 22px; background: var(--white); border-radius: 2px; }
  .search span { position: absolute; left: 6px; top: 3px; font-size: 12px; font-style: italic; color: #9aa3ad; font-family: "Arimo", sans-serif; }
  .search svg { position: absolute; right: 4px; top: 3px; }

  .panel-shadow { height: 22px; border-radius: 50%; background: radial-gradient(ellipse at center, rgba(0,0,0,0.16), rgba(0,0,0,0) 70%); }

  .quote-panel { left: 187px; top: 192px; width: 516px; height: 253px; border-radius: 4px; background: linear-gradient(var(--blue), var(--blue-dark)); color: var(--white); font-family: "Arimo", sans-serif; }
  .quote-title { position: absolute; left: 15px; top: 9px; font-family: "PT Sans", sans-serif; font-weight: 700; font-size: 22px; }
  .form-label { position: absolute; left: 9px; font-size: 14px; }
  .field { position: absolute; left: 197px; width: 305px; height: 21px; border: 1px solid rgba(255,255,255,0.15); background: rgba(255,255,255,0.04); font-size: 13px; padding: 2px 5px; }
  .field .caret { position: absolute; right: 0; top: 0; width: 17px; height: 19px; background: rgba(255,255,255,0.18); }
  .radio { position: absolute; font-size: 14px; display: flex; align-items: center; gap: 5px; }
  .radio i { width: 11px; height: 11px; border-radius: 50%; background: rgba(255,255,255,0.15); display: inline-block; }
  .radio i.on { background: radial-gradient(circle, var(--white) 35%, #8fb4d8 40%); }
  .quote-button { position: absolute; left: 9px; top: 207px; width: 162px; height: 35px; background: var(--white); color: var(--blue-dark); font-weight: 700; font-size: 14px; text-align: center; line-height: 37px; }

  .testimonials { left: 737px; top: 191px; width: 283px; height: 255px; background: linear-gradient(var(--green-light), var(--green-dark)); color: var(--white); }
  .testimonials h2 { position: absolute; width: 100%; top: 9px; text-align: center; font-size: 23px; font-weight: 700; }
  .rule { position: absolute; left: 16px; width: 251px; height: 1px; background: linear-gradient(90deg, rgba(255,255,255,0), rgba(255,255,255,0.5), rgba(255,255,255,0)); }
  .quote { position: absolute; left: 16px; width: 255px; font-size: 13.5px; font-weight: 700; line-height: 17px; }
  .quote cite { display: block; text-align: right; font-style: italic; margin-top: 1px; }

  .glance-title { left: 0; width: 1172px; top: 476px; text-align: center; font-size: 58px; font-weight: 700; color: var(--blue); }
  .glance-frame { left: 266px; top: 543px; width: 698px; height: 327px; border: 6px solid var(--blue-dark); border-radius: 3px; overflow: hidden; }
  .sky { position: absolute; inset: 0; background: linear-gradient(200deg, #3f7fde 0%, var(--sky-top) 35%, #a8cdf0 70%, var(--sky-pale) 100%); }
  .caption { position: absolute; left: 0; top: 217px; width: 638px; height: 110px; background: linear-gradient(90deg, rgba(255,255,255,0) 0%, rgba(255,255,255,0.55) 25%, rgba(255,255,255,0.45) 100%); }
  .caption p { position: absolute; left: 52px; top: 19px; width: 540px; text-align: center; font-size: 14.5px; line-height: 22px; color: var(--navy-text); }
  .accent { position: absolute; right: 0; top: 0; }

  .site-footer { left: 160px; top: 937px; width: 880px; height: 63px; background: linear-gradient(var(--blue), var(--blue-dark)); border: 3px solid var(--green); border-bottom: none; }
  .footer-link { position: absolute; top: 10px; font-size: 11px; font-weight: 700; color: var(--navy-text); }
  .copyright { position: absolute; width: 100%; top: 38px; left: -5px; text-align: center; font-size: 11px; font-weight: 700; color: var(--navy-text); }
</style>
</head>
<body>
  <header>
    <div class="abs brand"><span class="brand-name">KotaLindung</span><span class="brand-mark"></span></div>
    <div class="abs hotline">1-555-KOTALINDUNG</div>
  </header>

  <nav class="abs main-nav">
    <svg class="nav-home" width="128" height="27" viewBox="0 0 128 27">
      <defs><linearGradient id="tab" x1="0" y1="0" x2="0" y2="1"><stop offset="0" stop-color="#ffffff"/><stop offset="1" stop-color="#dce8f3"/></linearGradient></defs>
      <polygon points="0,0 128,0 100,27 0,27" fill="url(#tab)"/>
      <polygon points="112,0 128,0 100,27 82,27" fill="#9dd445"/>
    </svg>
    <span class="nav-item active" style="left:23px">Home</span>
    <span class="nav-item" style="left:131px">News</span>
    <span class="nav-item" style="left:238px">Quotes</span>
    <span class="nav-item" style="left:346px">Services</span>
    <span class="nav-item" style="left:454px">Contact</span>
    <div class="search"><span>Search</span>
      <svg width="16" height="16" viewBox="0 0 16 16"><circle cx="6.5" cy="6.5" r="5" fill="none" stroke="#3a7dbd" stroke-width="1.8"/><line x1="10" y1="10" x2="15" y2="15" stroke="#3a7dbd" stroke-width="2"/></svg>
    </div>
  </nav>

  <section class="abs quote-panel">
    <h1 class="quote-title">Cek Premi</h1>
    <span class="form-label" style="top:51px">Jenis Kendaraan:</span>
    <span class="form-label" style="top:77px">Tahun:</span>
    <span class="form-label" style="top:103px">Harga Pertanggungan:</span>
    <span class="form-label" style="top:127px">Kategori:</span>
    <span class="form-label" style="top:150px">Pertanggungan:</span>
    <div class="field" style="top:49px">:: Pilih Jenis ::<span class="caret"></span></div>
    <div class="field" style="top:75px">:: Pilih Tahun ::<span class="caret"></span></div>
    <div class="field" style="top:101px; left:193px">100,000,000</div>
    <span class="radio" style="left:203px; top:128px"><i class="on"></i>Pribadi</span>
    <span class="radio" style="left:283px; top:128px"><i></i>Dinas</span>
    <span class="radio" style="left:203px; top:151px"><i class="on"></i>Total Loss Only</span>
    <span class="radio" style="left:336px; top:151px"><i></i>Comprehensive</span>
    <div class="quote-button">Periksa Kutipan</div>
  </section>
  <div class="abs panel-shadow" style="left:195px; top:447px; width:520px"></div>

  <aside class="abs testimonials">
    <h2>Testimonials</h2>
    <div class="rule" style="top:63px"></div>
    <p class="quote" style="top:68px">KotaLindung offered me amazing insurance at an unbeatable price. I will definatley shop at KotaLindung again.<cite>-Budi S.</cite></p>
    <div class="rule" style="top:163px"></div>
    <p class="quote" style="top:168px">Lorem ipsum dolor sit amet, consectetur adipiscing elit. Donec egestas est non lacus sodales pharetra.<cite>-Lorem I.</cite></p>
  </aside>
  <div class="abs panel-shadow" style="left:737px; top:455px; width:285px"></div>

  <h2 class="abs glance-title">At A Glance</h2>
  <section class="abs glance-frame">
    <div class="sky" role="img" aria-label="Photo of a bright blue sky with soft white clouds"></div>
    <div class="caption"><p>Lorem ipsum dolor sit amet, consectetur adipiscing elit. Donec egestas est non lacus sodales pharetra. Etiam eu nibh vitae nisl condimentum iaculis vestibulum sed enim. Cras erat justo, dictum eu gravida et, sollicitudin ac sem.</p></div>
    <svg class="accent" width="70" height="315" viewBox="0 0 70 315">
      <polygon points="64,0 70,0 70,315 0,315" fill="#2f69a6"/>
      <polygon points="66,4 70,4 70,315 8,315" fill="#9dd445"/>
    </svg>
  </section>
  <div class="abs panel-shadow" style="left:255px; top:873px; width:745px; height:32px"></div>

  <footer class="abs site-footer">
    <span class="footer-link" style="left:299px">CONTACT</span>
    <span class="footer-link" style="left:371px">ABOUT</span>
    <span class="footer-link" style="left:442px">HOME</span>
    <span class="footer-link" style="left:515px">SERVICES</span>
    <span class="copyright">KotaLindung.com ©</span>
  </footer>
</body>
</html>
```